Water ATM Card

Need a design for water ATM cards. Size of card is 3.375 x 2.125 inch
On the Front include the Cedar Brook Logo.
Bottom right corner should have Price $100
On the Back
This card is to be used to access water refills at any Cedar Brook Water Vending Machines.
Please contact (869) 415 2983 or (869) 238 4617 or email clearflowhub@mailbox-example.com for any assistance or recharging of card.

```html
<!DOCTYPE html>
<html lang="en">
<head>
<meta charset="utf-8">
<title>Cedar Brook Water Card</title>
<link rel="stylesheet" href="https://fonts.googleapis.com/css2?family=Montserrat:wght@400;500;700&display=swap">
<style>
  :root {
    --stage: #1c1c1c;
    --card-white: #ffffff;
    --brand-blue: #1f5fae;
    --name-blue: #2a4a9e;
    --ink: #1a1a1a;
    --green: #3fae49;
    --back-top: #2f80c1;
    --back-mid: #3b5ea8;
    --back-bottom: #33418f;
    --white: #ffffff;
  }
  * { box-sizing: border-box; margin: 0; padding: 0; }
  html, body {
    width: 1200px; height: 1059px; overflow: hidden;
    background: var(--stage);
    font-family: "Montserrat", Arial, sans-serif;
  }
  .stage { position: relative; width: 1200px; height: 1059px; }
  .card {
    position: absolute; left: 256px; width: 690px; height: 394px;
    border-radius: 24px; overflow: hidden;
  }
  .card-front { top: 87px; background: var(--card-white); }
  .card-back {
    top: 546px;
    background: linear-gradient(160deg, var(--back-top) 0%, var(--back-mid) 35%, var(--back-bottom) 100%);
  }
  .brand-name {
    position: absolute; left: 38px; top: 50px;
    font-weight: 700; font-size: 27px; letter-spacing: 0.5px;
    color: var(--brand-blue); text-transform: uppercase;
  }
  .holder { position: absolute; right: 44px; top: 42px; text-align: right; }
  .holder-name {
    font-weight: 700; font-size: 23px; letter-spacing: 0.5px;
    color: var(--name-blue); text-transform: uppercase;
  }
  .holder-title { font-size: 15px; color: var(--ink); margin-top: 5px; letter-spacing: 0.5px; }
  .accent-bar {
    position: absolute; right: 0; top: 45px; width: 28px; height: 46px;
    background: var(--green);
  }
  .address {
    position: absolute; left: 38px; top: 181px;
    font-size: 15px; line-height: 18px; color: var(--ink);
  }
  .contacts { position: absolute; left: 38px; top: 250px; list-style: none; }
  .contacts li {
    display: flex; align-items: center; gap: 8px;
    font-size: 15px; color: var(--ink); height: 24px;
  }
  .contacts li:nth-child(2) { margin-top: 4px; }
  .contacts svg { width: 14px; height: 14px; fill: var(--brand-blue); flex: none; }
  .price {
    position: absolute; right: 37px; top: 208px;
    font-weight: 700; font-size: 20px; color: var(--green);
  }
  .back-name {
    position: absolute; left: 0; right: 0; top: 196px; text-align: center;
    font-weight: 700; font-size: 40px; letter-spacing: 1px;
    color: var(--white); text-transform: uppercase;
  }
  .back-note {
    position: absolute; left: 0; right: 0; top: 262px; text-align: center;
    font-size: 14px; line-height: 19px; color: var(--white);
  }
</style>
</head>
<body>
<main class="stage">
  <section class="card card-front" aria-label="Card front">
    <div class="brand-name">Cedar Brook</div>
    <div class="holder">
      <div class="holder-name">Daniel Hart</div>
      <div class="holder-title">OWER</div>
    </div>
    <div class="accent-bar"></div>
    <p class="address">480 Willow Ridge Drive, Ste<br>210 Maple Falls, TN 37890</p>
    <ul class="contacts">
      <li><svg viewBox="0 0 24 24"><path d="M6.6 10.8a15 15 0 0 0 6.6 6.6l2.2-2.2a1 1 0 0 1 1-.25 11.4 11.4 0 0 0 3.6.57 1 1 0 0 1 1 1V20a1 1 0 0 1-1 1A17 17 0 0 1 3 4a1 1 0 0 1 1-1h3.5a1 1 0 0 1 1 1c0 1.25.2 2.45.57 3.6a1 1 0 0 1-.25 1z"/></svg>(869) 415 2983</li>
      <li><svg viewBox="0 0 24 24"><path d="M7 1h10a2 2 0 0 1 2 2v18a2 2 0 0 1-2 2H7a2 2 0 0 1-2-2V3a2 2 0 0 1 2-2zm0 3v14h10V4zm5 15.5a1 1 0 1 0 0 2 1 1 0 0 0 0-2z"/></svg>(869) 238 4617</li>
      <li><svg viewBox="0 0 24 24"><path d="M2 5h20v2l-10 6L2 7zm0 4 10 6 10-6v10H2z"/></svg>clearflowhub@mailbox-example.com</li>
      <li><svg viewBox="0 0 24 24"><path d="M12 2a10 10 0 1 0 0 20 10 10 0 0 0 0-20zm-1 17.9A8 8 0 0 1 4.1 10L9 15v1a2 2 0 0 0 2 2zm6.9-2.5A2 2 0 0 0 16 16h-1v-3a1 1 0 0 0-1-1H8v-2h2a1 1 0 0 0 1-1V7h2a2 2 0 0 0 2-2v-.4a8 8 0 0 1 2.9 12.8z"/></svg>www.cedarbrookwater.example</li>
    </ul>
    <div class="price">Price $100</div>
  </section>

  <section class="card card-back" aria-label="Card back">
    <div class="back-name">Cedar Brook</div>
    <p class="back-note">This card is to be used to access water refills at any<br>Cedar Brook Water Vending Machines. Please contact<br>(869) 415 2983 or (869) 238 4617 or email<br>clearflowhub@mailbox-example.com<br>for any assistance or recharging of card.</p>
  </section>
</main>
</body>
</html>
```